New Company Business Card Design

I have a new company logo and I want a new business card design. I dont know if the logo file i attached is in the correct format or quality. We are a New York City Specialty construction Firm specializing in high risk out of the box projects. I want a simple and classy business card that people will his card is as crisp as the work his company does.

Target Market(s)

Clients in the heavy construction industry in New York City

Industry/Entity Type

Construction Company

Contact Information for Business Card

Simple Classy - DIFFERENT

Font styles to use
Other font styles liked:
• Mach the logo font in some way

Colors

Designer to choose colors to be used in the design.

Requirements
Must have
• Uniqueness
Nice to have
• Nothing particular - Just different and classy - Timeless
Should not have
• Goofy Shit or Gimmicky shit

```html
<!DOCTYPE html>
<html lang="en">
<head>
<meta charset="utf-8">
<title>Kestrel Builders, Inc. — Business Card</title>
<link rel="stylesheet" href="https://fonts.googleapis.com/css2?family=Open+Sans:wght@400;600;700;800&display=swap">
<style>
  :root {
    --stage: #2a2a2c;
    --card: #f7f7f7;
    --ink: #1d1d1f;
    --text-grey: #6b6b6b;
    --brand-blue: #1a63b3;
    --band-blue: #1f6fbf;
    --faint: #e4e4e4;
  }
  * { margin: 0; padding: 0; box-sizing: border-box; }
  html, body { width: 1200px; height: 840px; overflow: hidden; }
  body {
    background: var(--stage);
    font-family: "Open Sans", Arial, sans-serif;
    position: relative;
  }
  .card {
    position: absolute;
    width: 540px;
    height: 309px;
    background: var(--card);
    overflow: hidden;
    box-shadow: 0 6px 18px rgba(0,0,0,.35);
  }
  /* Back side */
  .card-back { left: 120px; top: 70px; }
  .back-illustration {
    position: absolute;
    left: 205px; top: 60px;
    width: 130px; height: 150px;
    background: linear-gradient(160deg, #3a3a3a, #111);
    opacity: .85;
  }
  .back-url {
    position: absolute;
    left: 0; right: 0; top: 232px;
    text-align: center;
    font-size: 11px;
    letter-spacing: 5px;
    color: var(--text-grey);
  }
  /* Front side */
  .card-front { left: 540px; top: 460px; }
  .front-illustration {
    position: absolute;
    left: 60px; top: 40px;
    width: 170px; height: 230px;
    background: linear-gradient(180deg, #e9e9e9, #dedede);
  }
  .company-name {
    position: absolute;
    right: 34px; top: 34px;
    font-size: 25px;
    font-weight: 800;
    color: var(--brand-blue);
    letter-spacing: .5px;
  }
  .person {
    position: absolute;
    right: 34px; top: 84px;
    text-align: right;
  }
  .person-name { font-size: 15px; font-weight: 700; color: var(--brand-blue); }
  .person-title { font-size: 11px; font-weight: 600; color: var(--ink); letter-spacing: .5px; }
  .contact {
    position: absolute;
    right: 34px; top: 132px;
    text-align: right;
    font-size: 11.5px;
    line-height: 19px;
    color: var(--text-grey);
  }
  .contact .label { color: var(--brand-blue); font-weight: 700; }
  .front-url {
    position: absolute;
    right: 34px; top: 230px;
    font-size: 11px;
    letter-spacing: 3px;
    color: var(--text-grey);
  }
  .front-band { position: absolute; left: 0; bottom: 0; }
</style>
</head>
<body>

<section class="card card-back" aria-label="Card back">
  <div class="back-illustration" role="img" aria-label="Crane illustration"></div>
  <p class="back-url">www.kestrelbuild.com</p>
</section>

<section class="card card-front" aria-label="Card front">
  <div class="front-illustration" role="img" aria-label="Faint crane illustration"></div>
  <h1 class="company-name">Kestrel Builders, Inc.</h1>
  <div class="person">
    <p class="person-name">DANIEL REYES</p>
    <p class="person-title">PRESIDENT</p>
  </div>
  <div class="contact">
    <p><span class="label">E:</span> daniel@kestrelbuild.com</p>
    <p><span class="label">F:</span> 212 555 0176</p>
    <p>4127 Harbor Lane Bayside, NY 11360</p>
    <p><span class="label">P:</span> 212 555 0148 <span class="label">M:</span> 917 555 0193</p>
  </div>
  <p class="front-url">www.kestrelbuild.com</p>
  <svg class="front-band" width="540" height="60" viewBox="0 0 540 60" aria-hidden="true">
    <polygon points="0,36 540,8 540,12 0,40" fill="var(--ink)"/>
    <polygon points="0,44 540,16 540,60 0,60" fill="var(--band-blue)"/>
  </svg>
</section>

</body>
</html>
```